MTSS Pyramid graphic needed for use in presentations and on my website

I am a consultant and need graphics to represent the MTSS pyramid (educational terminology) for use on my website and in slide decks. I've included documentation below that shows the MTSS pyramid, some preferences I have thought of, and my color palette. The MTSS pyramid is well-known in my field and I'd like one that I can use in all my presentations and on my website that looks professional and modern.

Target Market(s)

Educational leaders and educators

Industry/Entity Type

Educational Consulting

Font styles to use
Serif
Sans Serif

Colors
00AB8E
00BBA5
67D7C9
C6EFE9
E9F9F6
6B429C
8869AF
B7A5CE
E3DAEB
F3F0F8

Requirements
Must have
• a pyramid that can be recognized as an MTSS pyramid, use of colors that align with my color palette, a professional, modern look and feel, 3 sections with the largest at the bottom of the pyramid
Nice to have
• rounded corners, maybe 3D
Should not have
• a pyramid in a different shape or orientation, any more or fewer than 3 sections

```html
<!DOCTYPE html>
<html lang="en">
<head>
<meta charset="UTF-8">
<title>MTSS Pyramid</title>
<link href="https://fonts.googleapis.com/css2?family=Montserrat:wght@600;700&display=swap" rel="stylesheet">
<style>
  :root {
    --teal-dark: #00AB8E;
    --teal: #00BBA5;
    --violet-dark: #8869AF;
    --violet: #B7A5CE;
    --violet-light: #E3DAEB;
    --shelf: #5D6B80;
    --sky-top: #FFFFFF;
    --sky-bottom: #9CC4F6;
    --white: #FFFFFF;
  }
  * { margin: 0; padding: 0; box-sizing: border-box; }
  html, body { width: 1200px; height: 927px; overflow: hidden; }
  body {
    font-family: "Montserrat", Arial, sans-serif;
    background: linear-gradient(180deg, var(--sky-top) 0%, #FBFCFE 34%, #DCEAFC 56%, #B3D2F9 76%, var(--sky-bottom) 88%, var(--sky-bottom) 100%);
    position: relative;
  }
  .pyramid { position: absolute; left: 0; top: 0; width: 1200px; height: 927px; }
  .tier-tag { font-family: "Montserrat", Arial, sans-serif; font-weight: 700; fill: var(--white); }
  .tier-label {
    position: absolute;
    font-weight: 600;
    font-size: 27px;
    line-height: 33px;
    letter-spacing: 0.3px;
    white-space: nowrap;
  }
  .tier-label--intensive { left: 597px; top: 201px; color: var(--violet); }
  .tier-label--targeted { left: 674px; top: 342px; color: var(--violet-dark); }
  .tier-label--core { left: 767px; top: 516px; color: var(--teal-dark); }
</style>
</head>
<body>
  <svg class="pyramid" viewBox="0 0 1200 927" xmlns="http://www.w3.org/2000/svg" aria-label="Three-tier MTSS pyramid">
    <!-- Tier 1 -->
    <polygon fill="var(--shelf)" points="324,462 362,446 644,444 686,457 524,527"/>
    <polygon fill="var(--teal-dark)" points="324,462 524,527 537,748 210,640"/>
    <polygon fill="var(--teal)" points="524,527 686,457 796,631 537,748"/>
    <text class="tier-tag" font-size="36" transform="translate(596,622) rotate(-22)">Tier 1</text>

    <!-- Tier 2 -->
    <polygon fill="var(--shelf)" points="402,328 433,316 573,316 609,328 514,364"/>
    <polygon fill="var(--violet-dark)" points="402,328 514,364 520,496 329,435"/>
    <polygon fill="var(--violet)" points="514,364 609,328 676,431 520,496"/>
    <text class="tier-tag" font-size="23" transform="translate(548,431) rotate(-22)">Tier 2</text>

    <!-- Tier 3 -->
    <polygon fill="var(--violet)" points="504,179 514,340 407,309"/>
    <polygon fill="var(--violet-light)" points="504,179 598,304 514,340"/>
    <text class="tier-tag" font-size="14" transform="translate(522,310) rotate(-22)">Tier 3</text>
  </svg>

  <div class="tier-label tier-label--intensive">Intensive Individual<br>Intervention</div>
  <div class="tier-label tier-label--targeted">Targeted Intervention</div>
  <div class="tier-label tier-label--core">Core Instruction</div>
</body>
</html>
```